Dishcart

App Design for a an application on which you can order take aways from restaurants close to you.
(similar app : https://appvault.example/lu/app/brunomeal-pizza-burger-sushi/id538216047?l=en&mt=8 )

Logo is a taxi (psd of taxi an font attached)

Attached a draft mockup showing the screens needed.

Screens needed :

1. Splash Screen
2. Select you restaurant screen
3. Select your dish (meat, pizza, pasta....)
4. Select your extras (exta cheese, garlik etc...)
5. Exit screen with total amount and confirmation
6. Subscribe Screen where people have to register the first time.

Target Market(s)

age 14-54

Industry/Entity Type

Restaurant

Requirements
Must have
• Wood elements

```html
<!DOCTYPE html>
<html lang="en">
<head>
<meta charset="utf-8">
<title>Dishcart – Restaurants &amp; Pizzas</title>
<link rel="stylesheet" href="https://fonts.googleapis.com/css2?family=Open+Sans:wght@400;600&family=Antonio:wght@600&display=swap">
<style>
:root{
  --bg:#e4e4e4;
  --wood-dark:#141312;
  --wood-mid:#2a2725;
  --leather:#9b6b45;
  --leather-light:#b07e57;
  --stitch:#d9b58f;
  --card:#fbf8ef;
  --card-shade:#f1ebdc;
  --divider:#e2d9c4;
  --accent:#f5a50f;
  --star:#f7b512;
  --ink:#2b2b2b;
  --muted:#666058;
  --star-off:#cfcfcf;
  --chevron:#5a3a22;
  --tab:#050505;
  --icon:#9a9a9a;
}
*{box-sizing:border-box;margin:0;padding:0}
html,body{width:1200px;height:1000px;overflow:hidden}
body{background:var(--bg);font-family:"Open Sans",Arial,sans-serif;position:relative}

.screen{position:absolute;top:200px;width:406px;height:610px;overflow:hidden;
  background:repeating-linear-gradient(90deg,var(--wood-dark) 0 7px,var(--wood-mid) 7px 9px,var(--wood-dark) 9px 19px,#1f1d1b 19px 21px)}
.screen--restaurants{left:111px}
.screen--menu{left:689px;width:404px}

.header{position:absolute;top:3px;left:0;right:0;height:72px;
  background:linear-gradient(180deg,var(--leather-light),var(--leather));
  box-shadow:0 3px 6px rgba(0,0,0,.6)}
.header::after{content:"";position:absolute;inset:4px;border:1px dashed var(--stitch);opacity:.55}
.header__title{font-family:"Antonio","Arial Narrow",sans-serif;font-weight:600;color:#fff;text-transform:uppercase;text-shadow:0 1px 2px rgba(0,0,0,.5)}
.header--restaurants .header__title{position:absolute;top:9px;left:0;right:0;text-align:center;font-size:20px;line-height:26px}
.slider{position:absolute;left:78px;top:50px;width:254px;height:6px;border-radius:3px;background:#f7c21b;box-shadow:inset 0 1px 1px rgba(0,0,0,.3)}
.slider__knob{position:absolute;left:33px;top:-5px;width:16px;height:16px;border-radius:50%;background:radial-gradient(circle at 40% 35%,#fff,#bdbdbd);box-shadow:0 1px 2px rgba(0,0,0,.5)}
.header--menu .header__title{position:absolute;top:18px;left:146px;width:130px;text-align:center;font-size:31px;line-height:38px}
.back-button{position:absolute;left:18px;top:24px;width:94px;height:30px;z-index:1}
.back-button span{position:absolute;left:14px;top:6px;color:#fff;font-size:13px;font-weight:600}

.list{position:absolute;left:11px;top:91px;width:386px;height:456px;overflow:hidden;border-radius:6px 6px 0 0;background:var(--card)}
.restaurant{position:relative;height:84px;border-bottom:1px dashed var(--divider);background:linear-gradient(180deg,#fdfbf5,var(--card-shade))}
.restaurant__photo{position:absolute;left:11px;top:12px;width:64px;height:64px}
.restaurant__name{position:absolute;left:93px;top:7px;color:var(--accent);font-size:18px;font-weight:600}
.restaurant__cuisine{position:absolute;left:93px;top:30px;color:var(--ink);font-size:16px}
.rating{position:absolute;left:92px;top:52px;font-size:19px;line-height:22px;letter-spacing:0;color:var(--star)}
.rating .off{color:var(--star-off)}
.chevron{position:absolute;right:20px;top:28px;width:14px;height:28px}

.menu{position:absolute;left:11px;top:94px;width:383px;height:453px;overflow:hidden;border-radius:6px 6px 0 0;background:var(--card)}
.dish{position:relative;height:76px;border-bottom:1px dashed var(--divider);background:linear-gradient(180deg,#fdfbf5,var(--card-shade))}
.dish__name{position:absolute;left:13px;top:9px;color:var(--accent);font-size:18px;font-weight:600}
.dish__desc{position:absolute;left:13px;top:36px;width:260px;color:var(--ink);font-size:12.5px;line-height:15px}
.price{position:absolute;right:0;top:0;width:94px;height:100%;background:rgba(215,205,185,.35);padding:8px 0 0 12px;color:var(--muted);line-height:1}
.price small{display:block;font-size:9px;margin-bottom:3px}
.price b{display:block;font-weight:400;font-size:15px;margin-bottom:3px}

.tabbar{position:absolute;left:0;right:0;top:547px;height:63px;background:linear-gradient(180deg,#1a1a1a,var(--tab) 50%)}
.tabbar svg{position:absolute;top:16px;width:30px;height:30px}
</style>
</head>
<body>

<section class="screen screen--restaurants">
  <header class="header header--restaurants">
    <h1 class="header__title">12 restaurants dans mon enviroment</h1>
    <div class="slider"><div class="slider__knob"></div></div>
  </header>

  <ul class="list">
    <li class="restaurant">
      <div class="restaurant__photo" role="img" aria-label="Photo of a pizza" style="background:linear-gradient(135deg,#c9802f,#8b3b1c)"></div>
      <div class="restaurant__name">Casa Lucia</div>
      <div class="restaurant__cuisine">Italien</div>
      <div class="rating">★★★★<span class="off">★</span></div>
      <svg class="chevron" viewBox="0 0 14 28"><path d="M2 2l10 12L2 26" fill="none" stroke="var(--chevron)" stroke-width="2"/></svg>
    </li>
    <li class="restaurant">
      <div class="restaurant__photo" role="img" aria-label="Photo of a hamburger" style="background:linear-gradient(160deg,#e9d3b0,#a85a25 60%,#6d3b19)"></div>
      <div class="restaurant__name">Burger Ridge</div>
      <div class="restaurant__cuisine">American</div>
      <div class="rating">★★★<span class="off">★★</span></div>
      <svg class="chevron" viewBox="0 0 14 28"><path d="M2 2l10 12L2 26" fill="none" stroke="var(--chevron)" stroke-width="2"/></svg>
    </li>
    <li class="restaurant">
      <div class="restaurant__photo" role="img" aria-label="Photo of sushi on a board" style="background:linear-gradient(135deg,#d8c3a6,#c2553a 55%,#5a3a24)"></div>
      <div class="restaurant__name">Kaito</div>
      <div class="restaurant__cuisine">Japanese</div>
      <div class="rating">★★★★<span class="off">★</span></div>
      <svg class="chevron" viewBox="0 0 14 28"><path d="M2 2l10 12L2 26" fill="none" stroke="var(--chevron)" stroke-width="2"/></svg>
    </li>
    <li class="restaurant">
      <div class="restaurant__photo" role="img" aria-label="Photo of a Chinese stir-fry with rice" style="background:linear-gradient(160deg,#6b4a30,#e8e4dc 35%,#b5551f 70%,#5b7a2a)"></div>
      <div class="restaurant__name">Golden Lotus</div>
      <div class="restaurant__cuisine">Chinese</div>
      <div class="rating">★★★★<span class="off">★</span></div>
      <svg class="chevron" viewBox="0 0 14 28"><path d="M2 2l10 12L2 26" fill="none" stroke="var(--chevron)" stroke-width="2"/></svg>
    </li>
    <li class="restaurant">
      <div class="restaurant__photo" role="img" aria-label="Photo of Mexican wraps" style="background:linear-gradient(135deg,#d9a76a,#8a5a2e 60%,#4d6b2a)"></div>
      <div class="restaurant__name">Flor del Camino</div>
      <div class="restaurant__cuisine">Mexican</div>
      <div class="rating">★★★★<span class="off">★</span></div>
      <svg class="chevron" viewBox="0 0 14 28"><path d="M2 2l10 12L2 26" fill="none" stroke="var(--chevron)" stroke-width="2"/></svg>
    </li>
    <li class="restaurant">
      <div class="restaurant__photo" role="img" aria-label="Photo of a Russian dish" style="background:linear-gradient(135deg,#b0703a,#6a3d20)"></div>
      <div class="restaurant__name">Samovarka</div>
      <div class="restaurant__cuisine">Russian</div>
      <div class="rating">★★★★<span class="off">★</span></div>
      <svg class="chevron" viewBox="0 0 14 28"><path d="M2 2l10 12L2 26" fill="none" stroke="var(--chevron)" stroke-width="2"/></svg>
    </li>
  </ul>

  <nav class="tabbar">
    <svg style="left:76px" viewBox="0 0 30 30"><circle cx="12" cy="12" r="8" fill="none" stroke="var(--icon)" stroke-width="2.5"/><path d="M18 18l9 9" stroke="var(--icon)" stroke-width="3" stroke-linecap="round"/></svg>
    <svg style="left:188px" viewBox="0 0 30 30"><path d="M9 3v8M12 3v8M15 3v8M9 11q3 3 6 0M12 13v15" fill="none" stroke="var(--icon)" stroke-width="2"/><path d="M21 3q-4 6 0 12v13" fill="none" stroke="var(--icon)" stroke-width="3"/></svg>
    <svg style="left:292px" viewBox="0 0 30 30"><path d="M2 4h5l4 16h14l3-12H9" fill="none" stroke="var(--icon)" stroke-width="2.5"/><path d="M12 12h14M13 16h12" stroke="var(--icon)" stroke-width="1.5"/><circle cx="13" cy="25" r="2" fill="var(--icon)"/><circle cx="23" cy="25" r="2" fill="var(--icon)"/></svg>
  </nav>
</section>

<section class="screen screen--menu">
  <header class="header header--menu">
    <div class="back-button">
      <svg viewBox="0 0 94 30" width="94" height="30"><path d="M10 0H92a2 2 0 0 1 2 2V28a2 2 0 0 1-2 2H10L0 15Z" fill="#3a2618" stroke="#1e130b"/></svg>
      <span>Casa Lucia</span>
    </div>
    <h1 class="header__title">Pizzas</h1>
  </header>

  <ul class="menu">
    <li class="dish"><div class="dish__name">Margarita</div><div class="dish__desc">cheese and tomato</div>
      <div class="price"><small>from</small><b>5.50€</b><small>to</small><b>10.50€</b></div></li>
    <li class="dish"><div class="dish__name">Hawaiian pizza</div><div class="dish__desc">han and pineapple</div>
      <div class="price"><small>from</small><b>5.50€</b><small>to</small><b>10.50€</b></div></li>
    <li class="dish"><div class="dish__name">Siciliana pizza</div><div class="dish__desc">salami, pepperoni and beef</div>
      <div class="price"><small>from</small><b>5.50€</b><small>to</small><b>10.50€</b></div></li>
    <li class="dish"><div class="dish__name">Vegetali pizza</div><div class="dish__desc">onions, mushrooms, mixed peppers and sweetcorn</div>
      <div class="price"><small>from</small><b>5.50€</b><small>to</small><b>10.50€</b></div></li>
    <li class="dish"><div class="dish__name">Margarita</div><div class="dish__desc">cheese and tomato</div>
      <div class="price"><small>from</small><b>5.50€</b><small>to</small><b>10.50€</b></div></li>
    <li class="dish"><div class="dish__name">Margarita</div><div class="dish__desc">cheese and tomato</div>
      <div class="price"><small>from</small><b>5.50€</b><small>to</small><b>10.50€</b></div></li>
  </ul>

  <nav class="tabbar">
    <svg style="left:76px" viewBox="0 0 30 30"><circle cx="12" cy="12" r="8" fill="none" stroke="var(--icon)" stroke-width="2.5"/><path d="M18 18l9 9" stroke="var(--icon)" stroke-width="3" stroke-linecap="round"/></svg>
    <svg style="left:188px" viewBox="0 0 30 30"><path d="M9 3v8M12 3v8M15 3v8M9 11q3 3 6 0M12 13v15" fill="none" stroke="var(--icon)" stroke-width="2"/><path d="M21 3q-4 6 0 12v13" fill="none" stroke="var(--icon)" stroke-width="3"/></svg>
    <svg style="left:292px" viewBox="0 0 30 30"><path d="M2 4h5l4 16h14l3-12H9" fill="none" stroke="var(--icon)" stroke-width="2.5"/><path d="M12 12h14M13 16h12" stroke="var(--icon)" stroke-width="1.5"/><circle cx="13" cy="25" r="2" fill="var(--icon)"/><circle cx="23" cy="25" r="2" fill="var(--icon)"/></svg>
  </nav>
</section>

</body>
</html>
```